1200mm high x 900mm wide kids fitness poster for gym

I need an a poster designed to promote my kids/teenagers class.

This class is aimed at parents with kids between 10-15.

Design should be friendly and modern

Class is designed for kids that play sport and want to improve their fitness

Industry/Entity Type

Fitness

Font styles to use
Sans Serif

Colors

Designer to choose colors to be used in the design.

Requirements
Must have
• Text:
• Bright Stride teens program (TITLE)
• Improve: Performance, health, fitness, confidence, team mentality (BULLET POINTS)
• They will love our teen program! Contact us now to find out more:
• 1300452198
• enquiries@brightstride.fitness
• www.brightstride.fitness
• Must have friendly image of kids fitness or sport (FUN AND FRIENDLY IMAGE)

```html
<!DOCTYPE html>
<html lang="en">
<head>
<meta charset="utf-8">
<title>Bright Stride Teens Program</title>
<link href="https://fonts.googleapis.com/css2?family=Nunito:wght@800;900&family=Oswald:wght@600;700&display=swap" rel="stylesheet">
<style>
  :root {
    --navy: #1a5597;
    --blue: #1f86cf;
    --sky: #cfe6f7;
    --pale: #e6f3fc;
    --white: #ffffff;
    --ink: #1d4f8c;
  }
  html, body { margin: 0; padding: 0; overflow: hidden; }
  body { width: 900px; height: 1200px; background: var(--white); }
  .poster {
    position: relative; width: 900px; height: 1200px; overflow: hidden;
    background: repeating-linear-gradient(-3deg, var(--pale) 0 5px, #d9ecf9 5px 7px);
  }
  .hero-photo {
    position: absolute; left: 0; top: 0; width: 900px; height: 450px;
    background: linear-gradient(180deg, #e9eef2 0%, #d7dfe5 55%, #c9b8a6 100%);
  }
  .top-band { position: absolute; left: 0; top: 0; width: 900px; height: 460px; }
  .brand-header {
    position: absolute; left: 30px; top: 48px; display: flex; align-items: center; gap: 12px;
    font-family: 'Nunito', sans-serif; font-weight: 900; font-size: 28px; color: var(--white);
    letter-spacing: 0.5px;
  }
  .brand-dot { width: 30px; height: 30px; border-radius: 50%; background: var(--white); }
  .title-banner {
    position: absolute; left: 150px; top: 385px; width: 690px; height: 86px;
    background: var(--navy); border-radius: 18px;
    transform: rotate(-5deg); transform-origin: left bottom;
    box-shadow: 0 0 0 3px var(--pale), 0 0 0 5px var(--navy);
    display: flex; align-items: center; justify-content: center;
    font-family: 'Oswald', sans-serif; font-weight: 700; font-size: 44px; color: var(--white);
    letter-spacing: 0.5px;
  }
  .benefit {
    position: absolute; display: flex; align-items: center; gap: 6px;
    transform: rotate(-3deg);
    font-family: 'Nunito', sans-serif; font-weight: 900; font-size: 40px; color: var(--ink);
    text-shadow: 2px 2px 0 #9fc6e6;
  }
  .benefit svg { width: 72px; height: 68px; flex: none; }
  .rule-set { position: absolute; }
  .rule-set span { display: block; height: 3px; background: var(--navy); margin-bottom: 5px; }
  .photo-circle {
    position: absolute; border-radius: 50%;
    border: 5px solid var(--white); box-shadow: 0 0 0 4px var(--blue);
  }
  .contact-lead {
    position: absolute; left: 36px; top: 862px; width: 450px; text-align: center;
    font-family: 'Oswald', sans-serif; font-weight: 600; font-size: 26px; line-height: 40px;
    color: var(--navy);
  }
  .contact-row {
    position: absolute; left: 56px; display: flex; align-items: center; gap: 14px;
    font-family: 'Oswald', sans-serif; font-weight: 600; color: var(--navy);
  }
  .phone { top: 955px; font-size: 62px; font-weight: 700; }
  .web { top: 1058px; font-size: 26px; letter-spacing: 0.5px; }
  .mail { top: 1115px; font-size: 26px; }
  .left-frame { position: absolute; left: 0; top: 760px; width: 22px; height: 440px; background: var(--blue); border-top-right-radius: 16px; }
  .bottom-frame { position: absolute; left: 0; bottom: 0; width: 900px; height: 22px; background: var(--blue); }
  .brand-tab {
    position: absolute; left: 548px; top: 1108px; width: 380px; height: 80px;
    background: var(--white); border-top-left-radius: 40px;
    box-shadow: 0 0 0 4px var(--blue);
    display: flex; align-items: center; justify-content: center; gap: 12px;
    font-family: 'Nunito', sans-serif; font-weight: 900; font-size: 22px; color: var(--navy);
  }
  .brand-tab .brand-dot { background: var(--navy); width: 26px; height: 26px; }
</style>
</head>
<body>
<main class="poster">
  <div class="hero-photo" role="img" aria-label="Photo of three smiling teenage girls exercising with kettlebells and dumbbells in a bright gym studio"></div>

  <svg class="top-band" viewBox="0 0 900 460" aria-hidden="true">
    <path d="M0 0 H900 V16 H430 L410 0 Z" fill="#1f86cf"/>
    <path d="M0 0 H350 L320 100 Q312 122 290 122 H0 Z" fill="#1a5597"/>
    <path d="M330 0 H440 L420 16 H330 Z" fill="#1a5597" opacity="0"/>
    <polygon points="705,98 740,102 722,140" fill="#1f86cf" opacity="0.85"/>
    <polygon points="820,55 868,148 742,172" fill="#1f86cf" opacity="0.8"/>
    <path d="M0 378 H110 L0 520 Z" fill="#1a5597"/>
    <path d="M0 440 L900 370 V460 H0 Z" fill="#e6f3fc"/>
    <path d="M0 462 L900 368" stroke="#1f86cf" stroke-width="12"/>
  </svg>

  <div class="brand-header"><span class="brand-dot"></span>BRIGHT STRIDE</div>

  <div class="title-banner">BRIGHT STRIDE TEENS PROGRAM</div>

  <div class="benefit" style="left:94px; top:546px;">
    <svg viewBox="0 0 72 68"><polygon points="18,4 54,4 70,34 54,64 18,64 2,34" fill="#fff" stroke="#1a5597" stroke-width="4"/><path d="M16 42 L24 28 L34 32 L44 38 L56 40 L56 46 L16 46 Z" fill="#e8413a"/></svg>
    <span>Performance</span>
  </div>
  <div class="benefit" style="left:510px; top:516px;">
    <svg viewBox="0 0 72 68"><polygon points="18,4 54,4 70,34 54,64 18,64 2,34" fill="#fff" stroke="#1a5597" stroke-width="4"/><path d="M36 44 C20 34 22 22 30 22 C33 22 35 24 36 26 C37 24 39 22 42 22 C50 22 52 34 36 44 Z" fill="#e8413a"/></svg>
    <span>Health</span>
  </div>
  <div class="benefit" style="left:100px; top:636px;">
    <svg viewBox="0 0 72 68"><polygon points="18,4 54,4 70,34 54,64 18,64 2,34" fill="#fff" stroke="#1a5597" stroke-width="4"/><rect x="14" y="26" width="6" height="16" rx="2" fill="#1f86cf"/><rect x="52" y="26" width="6" height="16" rx="2" fill="#1f86cf"/><rect x="20" y="32" width="32" height="4" fill="#1a5597"/></svg>
    <span>Fitness</span>
  </div>
  <div class="benefit" style="left:516px; top:612px;">
    <svg viewBox="0 0 72 68"><polygon points="18,4 54,4 70,34 54,64 18,64 2,34" fill="#fff" stroke="#1a5597" stroke-width="4"/><path d="M26 18 H46 V28 C46 36 40 40 36 40 C32 40 26 36 26 28 Z" fill="#f5b623"/><rect x="33" y="40" width="6" height="6" fill="#f5b623"/><rect x="28" y="46" width="16" height="5" fill="#e8413a"/></svg>
    <span>Confidence</span>
  </div>
  <div class="benefit" style="left:106px; top:724px;">
    <svg viewBox="0 0 72 68"><polygon points="18,4 54,4 70,34 54,64 18,64 2,34" fill="#fff" stroke="#1a5597" stroke-width="4"/><circle cx="36" cy="34" r="5" fill="#f0c9a4"/><path d="M36 34 L20 20 M36 34 L52 20 M36 34 L20 48 M36 34 L52 48" stroke="#e8413a" stroke-width="5" stroke-linecap="round"/></svg>
    <span>Team Mindset</span>
  </div>

  <div class="rule-set" style="left:24px; top:826px; width:476px;"><span></span><span></span><span></span></div>
  <div class="rule-set" style="left:690px; top:996px; width:210px;"><span></span><span></span><span></span></div>

  <div class="photo-circle" style="left:494px; top:782px; width:126px; height:126px; background:linear-gradient(160deg,#c9a98a,#4f6b86);" role="img" aria-label="Photo of teens riding spin bikes in a gym class"></div>
  <div class="photo-circle" style="left:658px; top:740px; width:212px; height:212px; background:linear-gradient(150deg,#3b3f4a,#c7413a 70%,#2c2f37);" role="img" aria-label="Photo of a trainer coaching a teenage girl on a cable machine"></div>
  <div class="photo-circle" style="left:554px; top:940px; width:126px; height:126px; background:linear-gradient(160deg,#a8c3dc,#c23a33 60%,#6a4a3a);" role="img" aria-label="Photo of a coach and young athletes joining hands in a team huddle"></div>

  <div class="contact-lead">THEY WILL LOVE OUR TEEN PROGRAM!<br>CONTACT US NOW TO FIND OUT MORE:</div>

  <div class="contact-row phone">
    <svg width="62" height="64" viewBox="0 0 24 24" aria-hidden="true"><path d="M6.6 2.5l3 3.2-1.8 2.6c.9 2.6 3.3 5 5.9 5.9l2.6-1.8 3.2 3-1.8 3.6c-7.6-.4-13.3-6.1-13.7-13.7z" fill="none" stroke="#1a5597" stroke-width="1.4" stroke-linejoin="round"/></svg>
    <span>1300.452.198</span>
  </div>
  <div class="contact-row web">
    <svg width="40" height="40" viewBox="0 0 24 24" aria-hidden="true" fill="none" stroke="#1a5597" stroke-width="1.5"><circle cx="12" cy="12" r="10"/><ellipse cx="12" cy="12" rx="4.5" ry="10"/><path d="M2 12h20M4 6.5h16M4 17.5h16"/></svg>
    <span>WWW.BRIGHTSTRIDE.FITNESS</span>
  </div>
  <div class="contact-row mail">
    <svg width="44" height="34" viewBox="0 0 26 20" aria-hidden="true"><rect x="1" y="4" width="24" height="15" fill="#1a5597"/><path d="M1 4 L13 13 L25 4" stroke="#fff" stroke-width="1.5" fill="none"/><path d="M5 6 V1 H21 V6" stroke="#1a5597" stroke-width="1.5" fill="none"/></svg>
    <span>ENQUIRIES@BRIGHTSTRIDE.FITNESS</span>
  </div>

  <div class="left-frame"></div>
  <div class="bottom-frame"></div>
  <div class="brand-tab"><span class="brand-dot"></span>BRIGHT STRIDE</div>
</main>
</body>
</html>
```